Loyalty/Discount Card Design Project

Loyalty card design for pennynest.co.uk. Disregard current site graphics!! Open to all colors/concepts. Back and front. Will require all .ai files please. No need to round corners.

Illustrator (ai) card template included with bleed for your convenience.

Target Market(s)

Shoppers looking to save money locally

Requirements
Must have
• Front:
(i)Card name (PennyNest)
(ii)Tagline (for discounts and special offers in Haverhill)
(iii)URL (www.pennynest.co.uk)

Back:
(i)Space for barcode and QR code.
(ii)Dummy small print like a credit card
(iii)Signature strip.

Spec:

4/4 (cmyk)
300 dpi
ai files/eps files/

Nice to have
• Would like the design to say 'save money' even if the text wasn't present.

```html
<!DOCTYPE html>
<html lang="en">
<head>
<meta charset="utf-8">
<title>PennyNest Loyalty Card – Front and Back</title>
<link rel="stylesheet" href="https://fonts.googleapis.com/css2?family=Arimo:wght@400;700&display=swap">
<style>
  :root {
    --card-red: #9b0a12;
    --white: #ffffff;
    --ink: #111111;
    --trim-cyan: #35c4e0;
    --bleed-green: #8fd14f;
    --fold-pink: #e58fd0;
    --page: #ffffff;
    --fine-print: #f3d9da;
  }
  html, body {
    margin: 0;
    padding: 0;
    width: 923px;
    height: 1200px;
    overflow: hidden;
    background: var(--page);
  }
  .artboard {
    display: block;
    width: 923px;
    height: 1200px;
    font-family: "Arimo", Arial, sans-serif;
  }
  .card-base { fill: var(--card-red); }
  .trim-line { fill: none; stroke: var(--trim-cyan); stroke-width: 1; }
  .bleed-line { fill: none; stroke: var(--bleed-green); stroke-width: 0.6; stroke-dasharray: 3 2; }
  .fold-line { fill: none; stroke: var(--fold-pink); stroke-width: 0.6; stroke-dasharray: 3 2; }
  .white-band { fill: var(--white); }
  .card-name { fill: var(--white); font-weight: 700; font-size: 41px; letter-spacing: -0.5px; }
  .tagline { fill: var(--ink); font-size: 12.6px; }
  .site-url { fill: var(--white); font-size: 12.4px; }
  .site-url--small { font-size: 11px; }
  .box-label { fill: var(--ink); font-size: 12.6px; }
  .box-label--small { font-size: 9px; }
  .small-print { fill: var(--fine-print); font-size: 6.4px; }
  .brand-mark { fill: var(--white); font-weight: 700; font-size: 20px; letter-spacing: -0.3px; }
</style>
</head>
<body>
<svg class="artboard" viewBox="0 0 354 462" preserveAspectRatio="none" xmlns="http://www.w3.org/2000/svg">
  <defs>
    <linearGradient id="money-house-tones" x1="0" y1="0" x2="1" y2="1">
      <stop offset="0" stop-color="#e9c7c4"/>
      <stop offset="0.5" stop-color="#d8d3b8"/>
      <stop offset="1" stop-color="#b9c9b0"/>
    </linearGradient>
    <radialGradient id="purse-tones" cx="0.45" cy="0.55" r="0.6">
      <stop offset="0" stop-color="#d8302b"/>
      <stop offset="0.7" stop-color="#b01a1a"/>
      <stop offset="1" stop-color="#ffffff"/>
    </radialGradient>
  </defs>

  <!-- Front of card -->
  <g class="card card--front">
    <rect class="bleed-line" x="1" y="1" width="352" height="226"/>
    <rect class="card-base" x="4" y="0" width="348" height="224" rx="14"/>
    <rect class="trim-line" x="10" y="6" width="336" height="212" rx="10"/>
    <text class="card-name" x="335" y="58" text-anchor="end">PennyNest</text>
    <rect class="white-band" x="20" y="68" width="332" height="30"/>
    <text class="tagline" x="50" y="88">For Discounts and Special Offers in Haverhill</text>
    <rect x="170" y="92" width="170" height="114" fill="url(#money-house-tones)" role="img" aria-label="Photograph of a small house built from banknotes"/>
    <text class="site-url" x="28" y="204">www.pennynest.co.uk</text>
  </g>

  <!-- Back of card -->
  <g class="card card--back">
    <rect class="bleed-line" x="1" y="233" width="352" height="228"/>
    <rect class="card-base" x="4" y="236" width="348" height="226" rx="14"/>
    <rect class="trim-line" x="10" y="242" width="336" height="212" rx="10"/>
    <line class="fold-line" x1="14" y1="372" x2="14" y2="410"/>
    <line class="fold-line" x1="342" y1="372" x2="342" y2="410"/>
    <text class="site-url site-url--small" x="26" y="270">www.pennynest.co.uk</text>
    <rect class="white-band barcode-space" x="198" y="252" width="134" height="30"/>
    <text class="box-label" x="265" y="272" text-anchor="middle">for barcode</text>

    <rect class="white-band qr-space" x="26" y="288" width="60" height="60"/>
    <text class="box-label box-label--small" x="56" y="321" text-anchor="middle">for QR code</text>

    <g class="small-print">
      <text x="96" y="298">This card remains the property of PennyNest</text>
      <text x="96" y="307">and is not transferable. Show it at any</text>
      <text x="96" y="316">member shop to claim offers. Discounts may</text>
      <text x="96" y="325">change without notice. If found, please</text>
      <text x="96" y="334">return to any member shop or visit</text>
      <text x="96" y="343">www.pennynest.co.uk</text>
    </g>

    <rect class="white-band signature-strip" x="4" y="372" width="348" height="38"/>
    <text class="box-label" x="66" y="395">Signature strip</text>
    <rect x="222" y="328" width="106" height="84" fill="url(#purse-tones)" role="img" aria-label="Illustration of an open red purse with coins and a banknote"/>

    <g class="small-print">
      <text x="26" y="426">Valid only when signed. Terms and conditions</text>
      <text x="26" y="435">apply, see www.pennynest.co.uk for details.</text>
    </g>
    <text class="brand-mark" x="286" y="440" text-anchor="middle">PennyNest</text>
  </g>
</svg>
</body>
</html>
```